"leading industry company in search of a new web page"

we are searching for a clean, industry driven, engineered oriented web page design,

it need to be clean, and it need to have the chiefs company photo on the first page.
we are a mexican engineered company, we have 3 special sector specialties so in the front page we need to have a link to each one of these, and another one for CV "jobs" IM PUTING A COUPLE OD DESIGN IDEAL WITH OUR INFO SO YOU CAN PUT IT ALL TOGETHER

IM PUTING OUR LOGO AVAILABLE SO YOU CAN PUT IT IN THE PAGE

OUR WEB PAGE IS http://dravol.com.mx

Target Market(s)

INDUSTRY LIKES ENERGY AND PETROL
COMPANIES IN THE ENGINEERING BUSINESS

Industry/Entity Type

Industry

Requirements
Must have
• CLEAN DESIGN,
• HIRING AND CV DEDICATED MENU TAB
• THE 3 DIVISIONS OF THE COMPANY
• SOCIAL MEDIA ON THE BOTTOM "JUST FACEBOOK AND TWITTER"
Nice to have
• COHERENCE WITH THE LOGO COLORS

```html
<!DOCTYPE html>
<html lang="en">
<head>
<meta charset="utf-8">
<title>Dravol — Engineering Consulting</title>
<link href="https://fonts.googleapis.com/css2?family=PT+Sans:wght@400;700&display=swap" rel="stylesheet">
<style>
:root{
  --green:#5e9e0c;
  --green-light:#8cc31c;
  --red:#cc0033;
  --red-light:#e4466e;
  --grey:#6b6b6b;
  --grey-light:#8c8c8c;
  --text:#333333;
  --nav:#444444;
  --footer:#333333;
  --band:#dcdcdc;
  --white:#ffffff;
}
*{margin:0;padding:0;box-sizing:border-box}
html,body{width:1200px;height:1000px;overflow:hidden}
body{position:relative;font-family:"PT Sans",sans-serif;color:var(--text);
  background:linear-gradient(#c9c9c9 0,#e4e4e4 60%,#d8d8d8 100%)}
.header{position:absolute;left:0;top:0;width:1200px;height:152px;background:var(--white);
  box-shadow:0 3px 6px rgba(0,0,0,.25);z-index:2}
.brand{position:absolute;left:96px;top:40px;display:flex;align-items:center;gap:12px}
.brand-mark{width:62px;height:62px;border-radius:50%;background:var(--red)}
.brand-name{font-size:62px;font-weight:700;color:var(--green);line-height:1;letter-spacing:-1px}
.search{position:absolute;left:860px;top:17px;width:246px;height:30px;display:flex;border:1px solid #bcbcbc}
.search-field{flex:1;background:linear-gradient(#d6d6d6,#ececec)}
.search-button{width:59px;background:linear-gradient(#8a8a8a,#666);color:#fff;font-size:12px;font-weight:700;
  display:flex;align-items:center;justify-content:center}
.nav{position:absolute;right:99px;top:114px;display:flex;gap:30px;font-size:17px;color:var(--nav);text-transform:uppercase}
.nav .active{color:var(--green-light)}
.hero{position:absolute;left:96px;top:152px;width:1010px;height:321px;
  background:linear-gradient(#6e6a6e 0%,#a78a7e 35%,#d9a27a 60%,#6b6570 78%,#3d3f49 100%)}
.hero-panel{position:absolute;left:636px;top:142px;width:374px;height:153px;background:rgba(235,235,235,.82);
  text-align:right;padding:24px 19px 0 10px;font-size:17px;line-height:24.5px;color:var(--text)}
.hero-panel .inline-brand{color:var(--green);font-weight:700}
.hero-panel .more{display:block;margin-top:18px;font-weight:700}
.dots{position:absolute;left:18px;top:296px;display:flex;gap:10px}
.dots span{width:10px;height:10px;border-radius:50%;background:#9a9a9a}
.dots span:first-child{background:var(--green-light)}
.tab-band{position:absolute;left:0;top:473px;width:1200px;height:53px;
  background:linear-gradient(#e8e8e8,#cfcfcf);border-bottom:1px solid #aaa}
.tabs{position:absolute;left:96px;top:473px;width:1010px;height:53px;display:flex}
.tab{flex:1;display:flex;align-items:center;justify-content:center;font-size:18px;font-weight:700;
  text-transform:uppercase;border-left:1px solid #a5a5a5;text-shadow:0 1px 0 #fff}
.tab:last-child{border-right:1px solid #a5a5a5}
.tab.industrial{color:var(--green)}
.tab.administration{color:#b01d2c}
.tab.verification{color:#555}
.tab.jobs{color:#222}
.sectors{position:absolute;left:98px;top:526px;width:1007px;height:165px;display:flex}
.sector{width:252px;padding:16px 22px 0 22px;font-size:16px;line-height:21px;text-align:justify}
.sector .more{display:block;text-align:right;font-weight:700;margin-top:10px}
.sector.industrial{background:radial-gradient(circle at 55% 45%,var(--green-light),var(--green) 60%);color:#f3f7e6}
.sector.administration{background:radial-gradient(circle at 55% 45%,var(--red-light),var(--red) 60%);color:#fce6ec}
.sector.verification{background:radial-gradient(circle at 55% 45%,var(--grey-light),var(--grey) 60%);color:#e8e8e8}
.sector.jobs{background:var(--white);color:var(--text);width:251px}
.content{position:absolute;left:98px;top:691px;width:1007px;height:272px;
  background:linear-gradient(#f6f6f6,#ededed 70%,#d2d2d2);display:flex;gap:54px;padding:20px 0 0 22px}
.article{width:453px;font-size:16px;line-height:21px}
.article h2{font-size:18px;font-weight:400;letter-spacing:.5px;padding-bottom:6px;margin-bottom:12px;
  border-bottom:1px solid;border-image:linear-gradient(90deg,#333,transparent 80%) 1}
.article p+p{margin-top:3px}
.footer{position:absolute;left:0;top:963px;width:1200px;height:37px;background:var(--footer)}
.social{position:absolute;left:1011px;top:955px;display:flex;gap:12px}
.social span{width:32px;height:32px;border-radius:50%;background:#2f6fc0;border:2px solid #e6eef8}
</style>
</head>
<body>
<header class="header">
  <div class="brand"><span class="brand-mark"></span><span class="brand-name">dravol</span></div>
  <div class="search"><div class="search-field"></div><div class="search-button">Search</div></div>
  <nav class="nav"><span class="active">Home</span><span>About us</span><span>Solutions</span><span>Technologies</span><span>News</span></nav>
</header>

<section class="hero" role="img" aria-label="Photo of an offshore oil platform at sunset">
  <div class="hero-panel">
    <span class="inline-brand">dravol</span> provides premier consulting services for quality engineering in the nuclear, industrial and construction fields
    <span class="more">read more &gt;&gt;</span>
  </div>
  <div class="dots"><span></span><span></span><span></span></div>
</section>

<div class="tab-band"></div>
<div class="tabs">
  <div class="tab industrial">Industrial</div>
  <div class="tab administration">Administration</div>
  <div class="tab verification">Verification</div>
  <div class="tab jobs">Jobs</div>
</div>

<section class="sectors">
  <div class="sector industrial">Lorem ipsum dolor sit amet, consectetuer adipi elit, sed diam nonummy nibh euismod tincidunt ut<span class="more">read more &gt;&gt;</span></div>
  <div class="sector administration">Lorem ipsum dolor sit amet, consectetuer adipi elit, sed diam nonummy nibh euismod tincidunt ut<span class="more">read more &gt;&gt;</span></div>
  <div class="sector verification">Lorem ipsum dolor sit amet, consectetuer adipi elit, sed diam nonummy nibh euismod tincidunt ut<span class="more">read more &gt;&gt;</span></div>
  <div class="sector jobs">Lorem ipsum dolor sit amet, consectetuer adipi elit, sed diam nonummy nibh euismod tincidunt ut<span class="more">read more &gt;&gt;</span></div>
</section>

<section class="content">
  <article class="article">
    <h2>HEADLINE 1</h2>
    <p>is composed by a group of professionals of ample experience in the fields of technical assessment and management. Their main goal is to provide services so our clients can improve the quality and security of their products and installations.</p>
    <p>More than 210 qualified and certified professionals are committed in participating with the small, medium and big enterprises. Their prestige and credibility are backed by the biggest projects developed in Mexico during the last 32 years.</p>
  </article>
  <article class="article">
    <h2>HEADLINE 1</h2>
    <p>is composed by a group of professionals of ample experience in the fields of technical assessment and management. Their main goal is to provide services so our clients can improve the quality and security of their products and installations.</p>
    <p>More than 210 qualified and certified professionals are committed in participating with the small, medium and big enterprises. Their prestige and credibility are backed by the biggest projects developed in Mexico during the last 32 years.</p>
  </article>
</section>

<footer class="footer"></footer>
<div class="social"><span aria-label="Social link one"></span><span aria-label="Social link two"></span></div>
</body>
</html>
```